new roofing company card

New primary business card for roofing company.

Industry/Entity Type

Residential roofing/Specializing in Asphalt and Standing seam metal roofing

Contact Information for Business Card

Phone number is: 484 672 1058 Email: support@fennridgeroofworks.com website: www.fennridgeroofworks.com

Colors
EB3D1F
EC4F4E
F09395
F8D3D4
FCEDEE

```html
<!DOCTYPE html>
<html lang="en">
<head>
<meta charset="utf-8">
<title>Fennridge Roofworks – Business Card</title>
<link href="https://fonts.googleapis.com/css2?family=Questrial&display=swap" rel="stylesheet">
<style>
  :root {
    --brand-orange: #eb3d1f;
    --ink: #2b2b2b;
    --paper: #ffffff;
    --backdrop: #f1f1f1;
    --card-shadow: rgba(0, 0, 0, 0.18);
  }
  html, body {
    margin: 0;
    padding: 0;
    width: 1200px;
    height: 900px;
    overflow: hidden;
    background: var(--backdrop);
    font-family: "Questrial", "Century Gothic", sans-serif;
  }
  .stage {
    position: relative;
    width: 1200px;
    height: 900px;
  }
  .card {
    position: absolute;
    left: 320px;
    width: 560px;
    height: 320px;
    background: var(--paper);
    box-shadow: 0 10px 28px var(--card-shadow);
    overflow: hidden;
  }
  .card--front { top: 80px; }
  .card--back { top: 480px; }

  .wordmark {
    display: flex;
    align-items: center;
    gap: 10px;
    color: var(--ink);
    font-size: 25px;
    line-height: 1.1;
    letter-spacing: 0.5px;
    text-align: center;
  }
  .wordmark__square {
    width: 14px;
    height: 14px;
    background: var(--brand-orange);
    flex: none;
  }

  /* Front */
  .front__rule {
    position: absolute;
    top: 152px;
    height: 12px;
    background: var(--brand-orange);
  }
  .front__rule--left { left: 0; width: 128px; }
  .front__rule--right { right: 0; width: 128px; }
  .card--front .wordmark {
    position: absolute;
    left: 150px;
    width: 260px;
    top: 130px;
    justify-content: center;
  }

  /* Back */
  .back__logo-panel {
    position: absolute;
    left: 0;
    top: 0;
    width: 214px;
    height: 320px;
    border-top: 8px solid var(--brand-orange);
    border-bottom: 8px solid var(--brand-orange);
    box-sizing: border-box;
    display: flex;
    align-items: center;
    justify-content: center;
  }
  .card--back .wordmark {
    flex-direction: column;
    font-size: 22px;
    gap: 8px;
  }
  .back__contact-panel {
    position: absolute;
    left: 214px;
    top: 0;
    right: 0;
    bottom: 0;
    background: var(--brand-orange);
    color: var(--paper);
    padding: 136px 0 0 40px;
    box-sizing: border-box;
  }
  .contact__phone {
    font-size: 20px;
    margin: 0 0 6px;
    letter-spacing: 0.5px;
  }
  .contact__line {
    font-size: 15.5px;
    margin: 0 0 4px;
  }
</style>
</head>
<body>
<main class="stage">
  <section class="card card--front" aria-label="Business card front">
    <div class="front__rule front__rule--left"></div>
    <div class="wordmark">
      <span class="wordmark__square"></span>
      <span>Fennridge Roofworks</span>
    </div>
    <div class="front__rule front__rule--right"></div>
  </section>

  <section class="card card--back" aria-label="Business card back">
    <div class="back__logo-panel">
      <div class="wordmark">
        <span class="wordmark__square"></span>
        <span>Fennridge<br>Roofworks</span>
      </div>
    </div>
    <div class="back__contact-panel">
      <p class="contact__phone">484 672 1058</p>
      <p class="contact__line">support@fennridgeroofworks.com</p>
      <p class="contact__line">www.fennridgeroofworks.com</p>
    </div>
  </section>
</main>
</body>
</html>
```